Modern Billboard Ad for Criminal Defense Firm

10.5 x 36 We're looking for something to set us apart from the local competition. Looking for sleek and modern. We're a mid-sized firm in a small market city. We want to give the artist room to be creative on this one.
Thanks

Target Market(s)

Adult clients who have been charged with a crime/DWI

Industry/Entity Type

legal

Font styles to use
Serif
Sans Serif

Requirements
Must have
• Needs to have the firm name in large lettering. Law Offices of Marcus T Whitfield. “PLLC” does not have to be included. Phone number of (555) 384-1927 should be included but not the main focus.
Nice to have
• A call to action or something similar. “Don’t go it alone, call today.”, “ Arrested?”

```html
<!DOCTYPE html>
<html lang="en">
<head>
<meta charset="UTF-8">
<title>Law Offices of Marcus T Whitfield – Billboard</title>
<link rel="stylesheet" href="https://fonts.googleapis.com/css2?family=Alfa+Slab+One&family=Source+Sans+3:wght@600&display=swap">
<style>
  :root {
    --page-bg: #e6eaee;
    --band-blue: #1fa2d8;
    --band-blue-deep: #1786bd;
    --panel-white: #f7f7f7;
    --panel-shade: #dcdcdc;
    --ink: #0b0c0e;
    --tagline: #e2e7ec;
    --ring: #c9c9cc;
    --portrait-dark: #0c0d0f;
    --portrait-suit: #6d6f73;
  }
  html, body {
    margin: 0;
    padding: 0;
    width: 1200px;
    height: 835px;
    overflow: hidden;
    background: var(--page-bg);
  }
  .billboard {
    position: absolute;
    left: 20px;
    top: 270px;
    width: 1160px;
    height: 294px;
    display: block;
  }
  .headline {
    font-family: "Alfa Slab One", "Rockwell", serif;
    fill: var(--ink);
    font-size: 94px;
  }
  .tagline {
    font-family: "Source Sans 3", "Myriad Pro", sans-serif;
    font-weight: 600;
    font-size: 21px;
    fill: var(--tagline);
  }
</style>
</head>
<body>
<svg class="billboard" viewBox="0 0 1160 294" xmlns="http://www.w3.org/2000/svg">
  <defs>
    <radialGradient id="panel-light" cx="0.5" cy="0.3" r="0.75">
      <stop offset="0" stop-color="var(--panel-white)"/>
      <stop offset="1" stop-color="var(--panel-shade)"/>
    </radialGradient>
    <linearGradient id="band-tone" x1="0" y1="0" x2="1" y2="0">
      <stop offset="0" stop-color="var(--band-blue)"/>
      <stop offset="1" stop-color="var(--band-blue-deep)"/>
    </linearGradient>
    <radialGradient id="portrait-tone" cx="0.5" cy="0.45" r="0.6">
      <stop offset="0" stop-color="var(--portrait-suit)"/>
      <stop offset="1" stop-color="var(--portrait-dark)"/>
    </radialGradient>
  </defs>

  <rect class="panel" x="0" y="0" width="1160" height="294" fill="url(#panel-light)"/>
  <rect class="band band-top" x="0" y="0" width="1160" height="35" fill="url(#band-tone)"/>
  <rect class="band band-bottom" x="0" y="253" width="1160" height="41" fill="url(#band-tone)"/>

  <ellipse class="portrait-ring" cx="148" cy="149" rx="121" ry="141" fill="var(--ring)"/>
  <ellipse class="portrait" cx="148" cy="149" rx="117" ry="137" fill="url(#portrait-tone)"
           role="img" aria-label="Portrait photo of the attorney in a grey suit"/>

  <text class="headline" x="288" y="135" textLength="841" lengthAdjust="spacingAndGlyphs">LAW OFFICES OF</text>
  <text class="headline" x="288" y="228" textLength="841" lengthAdjust="spacingAndGlyphs">MARCUS T WHITFIELD</text>

  <text class="tagline" x="369" y="280">“Don’t go it alone, call today. Arrested?”</text>
  <text class="tagline" x="820" y="280">(555) 384-1927</text>
</svg>
</body>
</html>
```